New Q-Vora Loop Vs. Old Bulky Ankle Bracelets Comparison Chart

See q-vora.com Need a cool high tech design that shows comparison between the New Q-Vora Loop and the Old Bulky embarrassing ankle bracelets.
list basic functions both devices perform then list all the great features the new q-vora loop brings.
Features Both have
GPS TRACKING
GEO Fencing
EXECLUSION ZONES
INCLUSION ZONES
TAMPER ALERTS
FEATURES OF Q-VORA LOOP
Discrete wrist worn band no more embarrassing ankle bracelets
BIOMETRIC CHECK-INS VIA FACIAL
DYNAMIC REMOTE CHECK-INS
Monitoring Agencies and Enrollees are connected via frequent Video/Photo/Audio Check-ins. RECOGNITION VIDEO/PIC CHECKINS
LOOMCALL
VIDEO CONFERENCE WELFARE CHECKS ETC.
COMMUNICATION
COMPLIANCE ENFORCEMENT VIA TEXT VIDEO CHAT PHONE DYNAMIC REMOTE CHECK-INS
Monitoring Agencies and Enrollees are connected via frequent Video/Photo/Audio Check-ins.ñ

Target Market(s)

Courts,Attorneys,jails,probation and parole

Industry/Entity Type

electronic monitoring

Requirements
Must have
• Comparison of Q-Vora Loop and Ankle Bracelets
Nice to have
• High tech design

```html
<!DOCTYPE html>
<html lang="en">
<head>
<meta charset="utf-8">
<title>Q-Vora Loop vs Ankle Bracelets</title>
<link href="https://fonts.googleapis.com/css2?family=Oswald:wght@300;500;600&family=Montserrat:wght@400;500;600;700;800&display=swap" rel="stylesheet">
<style>
:root{
  --navy:#0f2f6b;
  --navy-deep:#0a2250;
  --charcoal:#4a4a4c;
  --ink:#2b2b2e;
  --panel:#ececee;
  --white:#ffffff;
  --stage:#e4e4e6;
  --photo-a:#8a6b52;
  --photo-b:#2e2a2a;
}
*{margin:0;padding:0;box-sizing:border-box}
html,body{width:1200px;height:2540px;overflow:hidden;background:var(--stage)}
body{position:relative;font-family:"Montserrat",sans-serif;color:var(--ink)}
.flyer{position:absolute;left:50px;top:493px;width:827px;height:1168px;background:var(--white);
  transform:scale(1.3301);transform-origin:top left;overflow:hidden;box-shadow:0 6px 20px rgba(0,0,0,.18)}
.abs{position:absolute}
.hero-band{left:0;top:110px;width:827px;height:360px;background:linear-gradient(100deg,var(--navy) 0%,var(--navy-deep) 60%)}
.hero-photo{left:470px;top:0;width:357px;height:470px;background:linear-gradient(160deg,var(--photo-a),var(--photo-b))}
.device-shot{left:345px;top:205px;width:275px;height:295px;border-radius:18px;background:linear-gradient(150deg,#5d7fb8,#1b1b1f 70%)}
.tagline{left:175px;top:43px;width:430px;height:67px;background:var(--charcoal);clip-path:polygon(0 0,92% 0,100% 100%,0 100%);
  color:var(--white);font-size:19px;line-height:23px;padding:10px 0 0 40px;font-weight:400;white-space:nowrap}
.brand{left:40px;top:50px;display:flex;align-items:center;gap:8px}
.brand-dot{width:30px;height:30px;border-radius:50%;background:var(--navy)}
.brand-name{font-family:"Oswald",sans-serif;font-weight:600;font-size:26px;color:var(--navy)}
.headline{left:58px;top:212px;color:var(--white);font-family:"Oswald",sans-serif;z-index:2;white-space:nowrap}
.headline .lead{font-weight:300;font-size:30px;letter-spacing:.5px;display:block;margin-bottom:6px}
.headline .big{font-weight:600;font-size:54px;line-height:60px;display:block;letter-spacing:-1px}
.tab{height:36px;background:var(--navy);color:var(--white);font-size:19px;padding:6px 12px;white-space:nowrap;clip-path:polygon(0 0,93% 0,100% 100%,0 100%)}
.tab b{font-weight:800}
.rule{height:1.5px;background:var(--navy)}
.icon-label{width:140px;text-align:center;font-size:13px;font-weight:600;color:var(--ink)}
.panel{left:0;top:680px;width:827px;height:310px;background:var(--panel)}
.feat{font-size:11.5px;line-height:14px;color:var(--ink)}
.feat.right{text-align:right;font-size:12.5px;line-height:16px}
.num{width:26px;height:26px;border-radius:50%;background:var(--navy);color:var(--white);font-size:11px;font-weight:700;
  display:flex;align-items:center;justify-content:center;border:2px solid var(--white);box-shadow:0 0 0 1.5px var(--navy)}
.watch-ring{left:322px;top:742px;width:190px;height:190px;border-radius:50%;background:var(--white);border:3px solid var(--navy)}
.watch-shot{left:352px;top:768px;width:130px;height:140px;border-radius:26px;background:linear-gradient(150deg,#3b3b40,#0c0c0e)}
.allday{left:60px;top:1022px;font-weight:800;font-size:44px;line-height:48px;color:var(--navy);letter-spacing:-2px}
.alcohol{left:175px;top:1030px;width:150px;height:30px;background:var(--navy);color:var(--white);font-weight:800;font-size:22px;padding:0 8px;line-height:30px;clip-path:polygon(0 0,88% 0,100% 50%,88% 100%,0 100%)}
.monitoring{left:178px;top:1060px;font-weight:800;font-size:22px;color:var(--navy)}
.pill{left:350px;top:1033px;width:420px;height:50px;border-radius:10px;background:var(--charcoal);color:var(--white);font-weight:700;font-size:24px;text-align:center;line-height:50px;white-space:nowrap}
.footer-left{left:0;top:1107px;width:340px;height:61px;background:var(--charcoal);clip-path:polygon(0 0,96% 0,100% 100%,0 100%)}
.footer-right{left:330px;top:1107px;width:497px;height:61px;background:var(--navy);clip-path:polygon(0 0,100% 0,100% 100%,3% 100%)}
.phone{left:55px;top:1118px;color:var(--white);font-weight:800;font-size:28px;display:flex;align-items:center;gap:6px;white-space:nowrap}
.contact{left:345px;top:1117px;color:var(--white);font-size:18px;line-height:21px}
.store{top:1120px;height:34px;border-radius:5px;background:#111;border:1px solid #888}
</style>
</head>
<body>
<div class="flyer">
  <div class="abs hero-band"></div>
  <div class="abs hero-photo" role="img" aria-label="Photo of a man wearing the wrist band while pouring coffee at home"></div>
  <div class="abs tagline">THE FUTURE OF ELECTRONIC<br>MONITORING IS WORN ON THE WRIST</div>
  <div class="abs brand"><span class="brand-dot"></span><span class="brand-name">Q-Vora</span></div>
  <div class="abs device-shot" role="img" aria-label="Product shot of the wrist band, two smartphones showing the monitoring app and map, and an ankle unit"></div>
  <div class="abs headline">
    <span class="lead">COMPARISON OF</span>
    <span class="big">Q-VORA LOOP</span>
    <span class="big">&amp; ANKLE</span>
    <span class="big">BRACELETS</span>
  </div>

  <div class="abs tab" style="left:58px;top:492px;width:245px">Features <b>Both Device</b></div>
  <div class="abs rule" style="left:300px;top:525px;width:470px"></div>

  <svg class="abs" style="left:0;top:540px" width="827" height="100" viewBox="0 0 827 100">
    <g fill="none" stroke="var(--navy)">
      <g transform="translate(122,47)"><circle r="41" stroke-width="3"/><circle r="35" stroke-width="1.5"/>
        <path d="M0 -16a9 9 0 0 1 9 9c0 8 -9 16 -9 16s-9 -8 -9 -16a9 9 0 0 1 9 -9z" fill="var(--navy)" stroke="none"/><circle cy="-7" r="3.5" fill="#fff" stroke="none"/>
        <ellipse cy="12" rx="18" ry="5" stroke-width="2"/></g>
      <g transform="translate(262,47)"><circle r="41" stroke-width="3"/><circle r="35" stroke-width="1.5"/>
        <g fill="var(--navy)" stroke="none"><rect x="-20" y="-14" width="5" height="28"/><rect x="-10" y="-10" width="4" height="24"/><rect x="-2" y="-16" width="4" height="30"/><rect x="6" y="-10" width="4" height="24"/><rect x="15" y="-14" width="5" height="28"/><rect x="-20" y="-4" width="40" height="3"/></g></g>
      <g transform="translate(407,47)"><circle r="41" stroke-width="3"/><circle r="35" stroke-width="1.5"/>
        <circle r="17" fill="var(--navy)" stroke="none"/><path d="M-17 0h34M0 -17v34" stroke="#fff" stroke-width="2"/><circle cx="10" cy="10" r="8" fill="#fff" stroke="var(--navy)" stroke-width="2"/></g>
      <g transform="translate(549,47)"><circle r="41" stroke-width="3"/><circle r="35" stroke-width="1.5"/>
        <path d="M-18 -2l8 16h20l8 -16" stroke-width="3"/><circle cy="-10" r="5" fill="var(--navy)" stroke="none"/><circle cx="-10" cy="-4" r="4" fill="var(--navy)" stroke="none"/><circle cx="10" cy="-4" r="4" fill="var(--navy)" stroke="none"/></g>
      <g transform="translate(696,47)"><circle r="41" stroke-width="3"/><circle r="35" stroke-width="1.5"/>
        <rect x="-4" y="-16" width="8" height="22" rx="4" fill="var(--navy)" stroke="none"/><circle cy="12" r="4" fill="var(--navy)" stroke="none"/>
        <path d="M-11 -8a12 12 0 0 0 0 16M11 -8a12 12 0 0 1 0 16M-17 -12a18 18 0 0 0 0 24M17 -12a18 18 0 0 1 0 24" stroke-width="2.2"/></g>
    </g>
  </svg>
  <div class="abs icon-label" style="left:52px;top:648px">GPS TRACKING</div>
  <div class="abs icon-label" style="left:192px;top:648px">GEO Fencing</div>
  <div class="abs icon-label" style="left:337px;top:648px">EXECLUSION ZONES</div>
  <div class="abs icon-label" style="left:479px;top:648px">INCLUSION ZONES</div>
  <div class="abs icon-label" style="left:626px;top:648px">TAMPER ALERTS</div>

  <div class="abs panel"></div>
  <div class="abs tab" style="left:58px;top:690px;width:305px;font-size:18px;padding-top:7px">FEATURES OF <b>Q-VORA LOOP</b></div>
  <div class="abs rule" style="left:360px;top:722px;width:410px"></div>

  <svg class="abs" style="left:0;top:740px" width="827" height="240" viewBox="0 0 827 240">
    <g fill="none" stroke="#777" stroke-width="1" stroke-dasharray="2 2">
      <path d="M70 30V228H360l35 -40"/>
      <path d="M90 40H332M90 82H326M90 112H322M90 170H330"/>
      <path d="M757 22V220H480l-25 -30"/>
      <path d="M740 38H500M740 68H505M740 122H510M740 180H505"/>
    </g>
  </svg>

  <div class="abs num" style="left:59px;top:745px">1</div>
  <div class="abs feat" style="left:104px;top:748px">Discrete wrist worn band no more<br>embarrassing ankle bracelets</div>
  <div class="abs num" style="left:59px;top:790px">2</div>
  <div class="abs feat" style="left:104px;top:795px">BIOMETRIC CHECK-INS VIA FACIAL</div>
  <div class="abs num" style="left:59px;top:821px">3</div>
  <div class="abs feat" style="left:104px;top:825px">DYNAMIC REMOTE CHECK-INS</div>
  <div class="abs num" style="left:59px;top:856px">4</div>
  <div class="abs feat" style="left:104px;top:855px">Monitoring Agencies and Enrollees<br>are connected via frequent Video/<br>Photo/Audio Check-ins. RECOGNITION<br>VIDEO/PIC CHECKINS</div>
  <div class="abs num" style="left:59px;top:924px">5</div>
  <div class="abs feat" style="left:104px;top:929px">LOOMCALL</div>

  <div class="abs watch-ring"></div>
  <div class="abs watch-shot" role="img" aria-label="Product photo of the black wrist band"></div>

  <div class="abs feat right" style="left:480px;top:743px;width:247px">VIDEO CONFERENCE<br>WELFARE CHECKS ETC.</div>
  <div class="abs num" style="left:737px;top:745px">6</div>
  <div class="abs feat right" style="left:480px;top:787px;width:247px">COMMUNICATION</div>
  <div class="abs num" style="left:737px;top:782px">7</div>
  <div class="abs feat right" style="left:480px;top:818px;width:247px">COMPLIANCE ENFORCEMENT<br>VIA TEXT VIDEO CHAT PHONE<br>DYNAMIC REMOTE CHECK-INS</div>
  <div class="abs num" style="left:737px;top:829px">8</div>
  <div class="abs feat right" style="left:480px;top:872px;width:247px">Monitoring Agencies and Enrollees<br>are connected via frequent Video/<br>Photo/Audio Check-ins.ñ</div>
  <div class="abs num" style="left:737px;top:873px">9</div>

  <svg class="abs" style="left:58px;top:998px" width="70" height="50" viewBox="0 0 70 50">
    <g fill="none" stroke="var(--navy)" stroke-width="3"><path d="M8 40A27 27 0 1 1 62 40"/><path d="M35 14v14h10"/></g>
  </svg>
  <div class="abs allday">24/7</div>
  <div class="abs alcohol">ALCOHOL</div>
  <div class="abs monitoring">MONITORING</div>
  <div class="abs pill">Advanced Electronic Monitoring</div>

  <div class="abs footer-left"></div>
  <div class="abs footer-right"></div>
  <div class="abs phone">
    <svg width="20" height="22" viewBox="0 0 24 24"><path d="M6.6 10.8a15 15 0 0 0 6.6 6.6l2.2-2.2a1 1 0 0 1 1-.25 11.4 11.4 0 0 0 3.6.57 1 1 0 0 1 1 1V20a1 1 0 0 1-1 1A17 17 0 0 1 3 4a1 1 0 0 1 1-1h3.5a1 1 0 0 1 1 1c0 1.25.2 2.45.57 3.57a1 1 0 0 1-.25 1z" fill="none" stroke="#fff" stroke-width="2"/></svg>
    1-888-555-0147
  </div>
  <div class="abs contact">info@q-vora.com<br>q-vora.com</div>
  <div class="abs store" style="left:545px;width:102px"></div>
  <div class="abs store" style="left:653px;width:112px"></div>
</div>
</body>
</html>
```